Letterhead Design Project

I need letterhead designed for my law firm. It would also be used for web based stuff as well.

Industry/Entity Type

Law Firm

```html
<!DOCTYPE html>
<html lang="en">
<head>
<meta charset="UTF-8">
<title>Harlow &amp; Vance Letterhead</title>
<link rel="stylesheet" href="https://fonts.googleapis.com/css2?family=Open+Sans:wght@400&display=swap">
<style>
  :root {
    --backdrop: #000000;
    --paper: #ffffff;
    --header-band: #000000;
    --navy: #27276e;
    --photo-dark: #3a3d48;
    --photo-warm: #6a3a34;
    --dash: #2e2e8c;
    --text-light: #ffffff;
  }
  * { margin: 0; padding: 0; box-sizing: border-box; }
  html, body {
    width: 1200px; height: 1000px; overflow: hidden;
    background: var(--backdrop);
    font-family: "Open Sans", Arial, sans-serif;
  }
  .letterhead {
    position: absolute; left: 264px; top: 27px;
    width: 672px; height: 943px;
    background: var(--paper);
  }
  .header-band {
    position: absolute; left: 0; top: 21px;
    width: 672px; height: 210px;
    background: var(--header-band);
  }
  .brand-block {
    position: absolute; left: 0; top: 0;
    width: 209px; height: 209px;
    background: var(--navy);
  }
  .firm-name {
    position: absolute; left: 0; top: 8px;
    width: 209px;
    color: var(--text-light);
    font-weight: 400; font-size: 19.5px;
    line-height: 28px; text-align: center;
  }
  .partner-photo { position: absolute; }
  .partner-photo--left {
    left: 15px; top: 95px; width: 71px; height: 88px;
    background: linear-gradient(180deg, #5a5d68 0%, var(--photo-dark) 100%);
  }
  .partner-photo--right {
    left: 127px; top: 95px; width: 75px; height: 93px;
    background: linear-gradient(180deg, #3b3740 0%, var(--photo-warm) 100%);
  }
  .contact {
    position: absolute; left: 422px; top: 10px;
    color: var(--text-light);
    font-style: normal;
    font-size: 19.5px; line-height: 28px;
  }
  .contact p + p { margin-top: 27px; }
  .dash-rule {
    position: absolute; left: 0; width: 672px; height: 9px;
    background: repeating-linear-gradient(to right, var(--dash) 0 10px, transparent 10px 24px);
  }
  .dash-rule--top { top: 237px; }
  .dash-rule--bottom { top: 910px; }
</style>
</head>
<body>
  <div class="letterhead">
    <header class="header-band">
      <div class="brand-block">
        <p class="firm-name">Harlow &amp; Vance<br>Law Firm</p>
        <div class="partner-photo partner-photo--left" role="img" aria-label="Portrait photo of a partner in a dark suit"></div>
        <div class="partner-photo partner-photo--right" role="img" aria-label="Portrait photo of a partner in a red top and dark jacket"></div>
      </div>
      <address class="contact">
        <p>P.O.BOX 51-9063<br>Lakeside,IL 61427</p>
        <p>(123)555-0148<br>harlowvance@mail.com</p>
        <p>www.harlowvance.com</p>
      </address>
    </header>
    <div class="dash-rule dash-rule--top"></div>
    <div class="dash-rule dash-rule--bottom"></div>
  </div>
</body>
</html>
```